Vodka label for New Brand called BELU Vodka

We need a label measuring 3.5 inches wide & 5 inches tall for this vodka bottle. The brand is "BELU Vodka". This should be the largest font on the label. "Handcrafted in the USA" should be on bottle in small font near the bottom. The tagline "Bringing Evenings Lively Upward" also needs to be included anywhere that makes sense in a smaller font than the brand name. Also in smaller font at the bottom/corners- "80 proof, 750 ml, 40% alc/vol" I value the human mind over AI, but am providing a couple designs that were AI generated to give you a better idea where to start and what we are looking for. Thank you!
Updates

Target Market(s)

21-45 year olds.

Industry/Entity Type

Alcohol

Colors
0054AA
0677BA
7BADD7
CADEEF
E8F1F8
EB3D1F
EC4F4E
F09395
F8D3D4
FCEDEE

Requirements
Should not have
• You can not use the US flag but can use elements of it.

```html
<!DOCTYPE html>
<html lang="en">
<head>
<meta charset="utf-8">
<title>BELU Vodka – Label</title>
<link rel="stylesheet" href="https://fonts.googleapis.com/css2?family=Alfa+Slab+One&family=Oswald:wght@500&family=Roboto+Condensed:wght@500;700&family=Roboto:wght@500&display=swap">
<style>
  :root {
    --navy: #1a1d4e;
    --navy-deep: #14174a;
    --blue: #0054AA;
    --blue-mid: #0677BA;
    --cyan: #22c8e8;
    --sky: #CADEEF;
    --mist: #E8F1F8;
    --red: #EB3D1F;
    --rose: #F09395;
    --blush: #FCEDEE;
    --white: #ffffff;
    --silver-dark: #8e9094;
    --silver-light: #f2f2f2;
    --ink: #1b1b1f;
  }
  html, body {
    margin: 0;
    padding: 0;
    width: 1044px;
    height: 1200px;
    overflow: hidden;
  }
  body {
    background: linear-gradient(180deg, #dfe6f2 0%, #eef2f9 50%, #c9d4e6 100%);
    position: relative;
    font-family: "Roboto Condensed", sans-serif;
  }
  .label {
    position: absolute;
    left: 170px;
    top: 25px;
    width: 705px;
    height: 1150px;
  }
  .label-shapes {
    position: absolute;
    inset: 0;
  }
  .seal-name {
    position: absolute;
    left: 252px;
    top: 155px;
    width: 200px;
    text-align: center;
    font-family: "Alfa Slab One", serif;
    font-size: 44px;
    line-height: 50px;
    color: var(--white);
  }
  .brand-name {
    position: absolute;
    left: 0;
    top: 330px;
    width: 705px;
    text-align: center;
    font-family: "Alfa Slab One", serif;
    font-size: 150px;
    line-height: 190px;
    color: var(--navy);
    text-shadow: 3px 2px 0 var(--red);
    margin: 0;
    font-weight: 400;
  }
  .brand-rule {
    position: absolute;
    top: 426px;
    height: 3px;
    width: 62px;
    background: var(--navy);
  }
  .brand-rule.left { left: 45px; }
  .brand-rule.right { left: 597px; }
  .brand-kind {
    position: absolute;
    left: 0;
    top: 530px;
    width: 705px;
    text-align: center;
    font-family: "Oswald", sans-serif;
    font-weight: 500;
    font-size: 84px;
    line-height: 100px;
    letter-spacing: 44px;
    text-indent: 44px;
    color: var(--navy);
  }
  .tagline {
    position: absolute;
    left: 240px;
    top: 660px;
    width: 225px;
    text-align: center;
    font-family: "Roboto Condensed", sans-serif;
    font-weight: 500;
    font-size: 38px;
    line-height: 47px;
    color: var(--ink);
    margin: 0;
  }
  .origin {
    position: absolute;
    left: 142px;
    top: 905px;
    width: 401px;
    height: 48px;
    line-height: 50px;
    text-align: center;
    font-family: "Roboto Condensed", sans-serif;
    font-weight: 700;
    font-size: 27px;
    letter-spacing: 2px;
    color: var(--white);
  }
  .stat {
    position: absolute;
    top: 975px;
    width: 124px;
    text-align: center;
    color: var(--white);
  }
  .stat.proof { left: 40px; }
  .stat.abv { left: 180px; }
  .stat-value {
    display: block;
    font-family: "Roboto", sans-serif;
    font-weight: 500;
    font-size: 50px;
    line-height: 52px;
  }
  .stat-value small { font-size: 28px; }
  .stat-unit {
    display: block;
    font-family: "Roboto", sans-serif;
    font-weight: 500;
    font-size: 20px;
    line-height: 24px;
    letter-spacing: 1px;
  }
  .quality {
    position: absolute;
    left: 340px;
    top: 985px;
    width: 310px;
    text-align: right;
    font-family: "Roboto Condensed", sans-serif;
    font-weight: 700;
    font-size: 30px;
    letter-spacing: 2px;
    color: var(--ink);
  }
  .volume {
    position: absolute;
    left: 440px;
    top: 1057px;
    width: 205px;
    text-align: right;
    font-family: "Roboto", sans-serif;
    font-weight: 500;
    font-size: 36px;
    line-height: 44px;
    color: var(--white);
  }
</style>
</head>
<body>
  <main class="label">
    <svg class="label-shapes" width="705" height="1150" viewBox="0 0 705 1150" aria-hidden="true">
      <defs>
        <linearGradient id="band-sheen" x1="0" y1="0" x2="1" y2="0">
          <stop offset="0" stop-color="var(--navy-deep)"/>
          <stop offset="0.15" stop-color="var(--cyan)"/>
          <stop offset="0.4" stop-color="var(--navy-deep)"/>
          <stop offset="0.65" stop-color="var(--blue-mid)"/>
          <stop offset="1" stop-color="var(--navy-deep)"/>
        </linearGradient>
        <linearGradient id="arch-sheen" x1="0" y1="0" x2="1" y2="0">
          <stop offset="0" stop-color="var(--navy-deep)"/>
          <stop offset="0.45" stop-color="var(--cyan)"/>
          <stop offset="1" stop-color="var(--navy-deep)"/>
        </linearGradient>
        <linearGradient id="silver" x1="0" y1="0" x2="1" y2="0">
          <stop offset="0" stop-color="var(--silver-dark)"/>
          <stop offset="0.3" stop-color="var(--silver-light)"/>
          <stop offset="0.55" stop-color="#bdbec2"/>
          <stop offset="0.8" stop-color="var(--silver-light)"/>
          <stop offset="1" stop-color="var(--silver-dark)"/>
        </linearGradient>
        <linearGradient id="shield-silver" x1="0" y1="0" x2="1" y2="0">
          <stop offset="0" stop-color="#9c9ea2"/>
          <stop offset="0.5" stop-color="var(--silver-light)"/>
          <stop offset="1" stop-color="#9c9ea2"/>
        </linearGradient>
        <linearGradient id="shield-rim" x1="0" y1="0" x2="1" y2="1">
          <stop offset="0" stop-color="var(--cyan)"/>
          <stop offset="0.5" stop-color="var(--navy-deep)"/>
          <stop offset="1" stop-color="var(--blue-mid)"/>
        </linearGradient>
        <linearGradient id="flag-wash" x1="0" y1="0" x2="1" y2="1">
          <stop offset="0" stop-color="var(--sky)"/>
          <stop offset="0.35" stop-color="var(--mist)"/>
          <stop offset="0.55" stop-color="var(--blush)"/>
          <stop offset="1" stop-color="var(--rose)"/>
        </linearGradient>
        <radialGradient id="stat-ring" cx="0.5" cy="0.5" r="0.5">
          <stop offset="0.8" stop-color="var(--navy)"/>
          <stop offset="0.92" stop-color="var(--cyan)"/>
          <stop offset="1" stop-color="var(--navy-deep)"/>
        </radialGradient>
      </defs>

      <rect class="panel" x="0" y="100" width="705" height="835" fill="var(--white)"/>
      <rect class="flag-motif" x="0" y="100" width="705" height="835" fill="url(#flag-wash)" opacity="0.75"
            role="img" aria-label="Soft waving stars and stripes motif in pale blue and red"/>

      <path class="top-band" d="M0 80 H240 A150 150 0 0 1 464 80 H705 V100 H461 A135 135 0 0 0 243 100 H0 Z" fill="url(#arch-sheen)"/>

      <circle class="seal" cx="352" cy="180" r="137" fill="var(--navy)"/>
      <circle class="seal-ring" cx="352" cy="180" r="124" fill="none" stroke="var(--blue)" stroke-width="10"/>
      <circle class="seal-inner" cx="352" cy="180" r="102" fill="var(--navy)" stroke="var(--white)" stroke-width="4"/>

      <path class="shield" d="M240 638 H465 V790 Q465 872 352 890 Q240 872 240 790 Z"
            fill="url(#shield-silver)" stroke="url(#shield-rim)" stroke-width="9"/>

      <rect class="origin-tab" x="142" y="905" width="401" height="48" fill="var(--navy)"/>
      <rect class="rule-band" x="0" y="935" width="705" height="20" fill="var(--navy)"/>
      <rect class="silver-band" x="0" y="955" width="705" height="95" fill="url(#silver)"/>
      <rect class="navy-band" x="0" y="1050" width="705" height="55" fill="var(--navy)"/>
      <rect class="sheen-band" x="0" y="1105" width="705" height="25" fill="url(#band-sheen)"/>

      <circle class="stat-badge" cx="102" cy="1030" r="63" fill="url(#stat-ring)"/>
      <circle class="stat-badge" cx="242" cy="1030" r="63" fill="url(#stat-ring)"/>
    </svg>

    <div class="seal-name">BELU</div>

    <span class="brand-rule left"></span>
    <h1 class="brand-name">BELU</h1>
    <span class="brand-rule right"></span>
    <div class="brand-kind">VODKA</div>

    <p class="tagline">BRINGING<br>EVENINGS<br>LIVELY<br>UPWARD</p>

    <div class="origin">HANDCRAFTED IN THE USA</div>

    <div class="stat proof">
      <span class="stat-value">80</span>
      <span class="stat-unit">PROOF</span>
    </div>
    <div class="stat abv">
      <span class="stat-value">40<small>%</small></span>
      <span class="stat-unit">alc/vol</span>
    </div>

    <div class="quality">PREMIUM QUALITY</div>
    <div class="volume">750ml</div>
  </main>
</body>
</html>
```